Designing our 2018 Look Book! New help with slide design and picture layout

We create a yearly "Look book" with all of our season's designs for the year and need creative help creating the design and layout of the book

Need help with the slide design and picture layout

Target Market(s)

Property managers and office managers

Requirements
Must have
• layout of the photos and design of cover slide templates
• See our logo attached (color scheme and you can use the logo as well)
• Also see our website for our "look" www.dunvoria.com

```html
<!DOCTYPE html>
<html lang="en">
<head>
<meta charset="utf-8">
<title>Dunvoria Look Book</title>
<link href="https://fonts.googleapis.com/css2?family=Lato:wght@400;700;900&family=Montserrat:wght@600;700&display=swap" rel="stylesheet">
<style>
  :root{
    --leaf:#7dbb42;
    --forest:#4f8a2b;
    --mint:#e6f1da;
    --paper:#ffffff;
    --ink:#3b3d3f;
    --muted:#7d8084;
    --backdrop:#d7d9db;
  }
  *{box-sizing:border-box;margin:0;padding:0}
  html,body{width:726px;height:1200px;overflow:hidden}
  body{background:var(--backdrop);font-family:'Lato',sans-serif;color:var(--ink);position:relative}
  .sheet{position:absolute;background:var(--paper);box-shadow:0 3px 10px rgba(0,0,0,.18);overflow:hidden}
  .cover{left:173px;top:20px;width:380px;height:260px}
  .spread{left:33px;width:660px;height:245px}
  .spread .page{position:absolute;top:0;width:330px;height:245px;overflow:hidden}
  .spread .page.left{left:0}
  .spread .page.right{left:330px;border-left:1px solid #e4e4e4}
  .spread-covers{top:305px}
  .spread-about{top:580px}
  .spread-plants{top:855px}
  .photo{position:absolute}
  .brand{position:absolute;font-family:'Montserrat',sans-serif;font-weight:700;color:var(--leaf);display:flex;align-items:center;gap:5px;letter-spacing:.2px}
  .brand .dot{width:8px;height:8px;border-radius:50%;background:var(--leaf)}
  .cover-band{position:absolute;background:var(--leaf);color:#fff}
  .cover-band h2{font-family:'Montserrat',sans-serif;font-weight:700;line-height:1.05}
  .cover-band p{line-height:1.2}
  .url-tab{position:absolute;background:var(--leaf);color:#fff;font-size:7px;font-weight:700;display:flex;align-items:center;justify-content:center}
  .back-panel{position:absolute;background:var(--leaf);color:#fff;padding:9px}
  .back-panel h3{font-size:9px;font-weight:900;margin-bottom:4px}
  .back-panel p{font-size:6.5px;line-height:1.35}
  .edge-strip{position:absolute;top:0;right:0;width:14px;height:100%;background:var(--leaf)}
  .heading{font-family:'Montserrat',sans-serif;color:var(--leaf);font-weight:700}
  .kicker{font-size:7.5px;font-weight:900;color:var(--forest);letter-spacing:.6px}
  .body{font-size:6px;line-height:1.45;color:var(--muted)}
  .item h4{font-size:6px;font-weight:900;color:var(--forest);letter-spacing:.4px;margin-bottom:1px}
  .gallery{position:absolute;left:22px;top:38px;width:290px;display:grid;grid-template-columns:repeat(4,1fr);gap:8px 10px}
  .plant{display:flex;flex-direction:column;align-items:center;gap:3px}
  .plant .pot{width:44px;height:42px;border-radius:4px;background:linear-gradient(180deg,#6fa84a 0%,#4d7f33 65%,#9a9c9e 66%,#77797b 100%)}
  .plant span{font-size:5.5px;color:var(--muted)}
  .round{position:absolute;width:34px;height:34px;border-radius:50%;background:radial-gradient(#7db257,#3f6e2a)}
</style>
</head>
<body>

<!-- Closed cover -->
<section class="sheet cover">
  <div class="brand" style="left:150px;top:18px;font-size:20px"><span class="dot"></span>Dunvoria</div>
  <div class="photo" role="img" aria-label="Office lounge with a dark doorway, grey sofa and tall potted plants" style="left:0;top:62px;width:380px;height:130px;background:linear-gradient(90deg,#eef0ef 0%,#cfd3d2 35%,#9ea3a3 55%,#e3e5e3 80%,#6f9f4e 100%)"></div>
  <div class="cover-band" style="left:0;top:168px;width:200px;height:62px;padding:8px 12px">
    <h2 style="font-size:14px">Growth Hackers</h2>
    <p style="font-size:9px;margin-top:3px">Create a healthy, productive workspace through plants.</p>
  </div>
  <div class="url-tab" style="right:0;top:236px;width:110px;height:12px">www.dunvoria.com</div>
</section>

<!-- Back and front covers -->
<section class="sheet spread spread-covers">
  <div class="page left">
    <div class="brand" style="left:16px;top:14px;font-size:14px"><span class="dot"></span>Dunvoria</div>
    <div class="back-panel" style="left:16px;top:52px;width:120px;height:120px">
      <h3>Greener offices, happier teams.</h3>
      <p>Plant design, care and maintenance for modern workplaces.</p>
      <p style="margin-top:30px;font-weight:700">www.dunvoria.com</p>
    </div>
    <div class="photo" role="img" aria-label="Potted green plants arranged on a low white planter" style="left:136px;top:52px;width:178px;height:120px;background:linear-gradient(180deg,#dfe3df 0%,#a9bf95 45%,#5f8f3f 70%,#d8d8d6 100%)"></div>
  </div>
  <div class="page right">
    <div class="brand" style="left:120px;top:14px;font-size:16px"><span class="dot"></span>Dunvoria</div>
    <div class="photo" role="img" aria-label="Office lounge with a dark doorway, grey sofa and tall potted plants" style="left:0;top:52px;width:330px;height:120px;background:linear-gradient(90deg,#eef0ef 0%,#cfd3d2 35%,#9ea3a3 55%,#e3e5e3 80%,#6f9f4e 100%)"></div>
    <div class="cover-band" style="left:0;top:150px;width:170px;height:54px;padding:7px 10px">
      <h2 style="font-size:12px">Growth Hackers</h2>
      <p style="font-size:7.5px;margin-top:2px">Create a healthy, productive workspace through plants.</p>
    </div>
    <div class="url-tab" style="right:0;top:214px;width:96px;height:11px">www.dunvoria.com</div>
  </div>
</section>

<!-- About spread -->
<section class="sheet spread spread-about">
  <div class="page left">
    <div class="photo" role="img" aria-label="Bright meeting room with white chairs, long table and wall screen" style="left:0;top:0;width:330px;height:245px;background:linear-gradient(160deg,#f4f4f2 0%,#dcdcd9 45%,#b9bbbc 75%,#8f9396 100%)"></div>
  </div>
  <div class="page right">
    <h2 class="heading" style="position:absolute;left:18px;top:18px;font-size:16px">About us</h2>
    <div class="kicker" style="position:absolute;left:18px;top:40px">A NATURAL<br>EVOLUTION</div>
    <p class="body" style="position:absolute;left:140px;top:22px;width:160px">We started with one idea: bring living plants into every office and let them work for the people inside. Today our team designs, installs and cares for planted spaces across the city.</p>
    <div class="photo" role="img" aria-label="Group photo of the company team in their office" style="left:18px;top:100px;width:150px;height:95px;background:linear-gradient(180deg,#c9cbc6 0%,#7f8478 55%,#3f4540 100%)"></div>
    <div class="item" style="position:absolute;left:180px;top:100px;width:125px">
      <h4>FRIENDLY PROFESSIONAL SERVICE</h4>
      <p class="body">Every visit is handled by our own trained plant technicians.</p>
    </div>
    <div class="item" style="position:absolute;left:180px;top:138px;width:125px">
      <h4>OUR MISSION</h4>
      <p class="body">To make workplaces healthier, calmer and more productive.</p>
    </div>
    <div class="item" style="position:absolute;left:180px;top:170px;width:125px">
      <h4>OUR VALUES</h4>
      <p class="body">Care, honesty and a love of green things.</p>
    </div>
    <div class="edge-strip"></div>
  </div>
</section>

<!-- Plants spread -->
<section class="sheet spread spread-plants">
  <div class="page left">
    <div class="photo" role="img" aria-label="Living green wall inside an office" style="left:0;top:0;width:90px;height:245px;background:linear-gradient(180deg,#8a6a3a 0%,#4f7d32 30%,#2f5a24 100%)"></div>
    <div class="kicker" style="position:absolute;left:104px;top:18px;color:var(--leaf)">WHY PLANTS?</div>
    <h2 class="heading" style="position:absolute;left:104px;top:30px;width:200px;font-size:12px;line-height:1.15">Let's plant some happiness — and grow fresh air together</h2>
    <p class="body" style="position:absolute;left:104px;top:78px;width:205px;font-weight:700;color:var(--ink)">Plants do more than look good in your space.</p>
    <p class="body" style="position:absolute;left:104px;top:92px;width:205px">They clean the air, soften noise and lift the mood of everyone who works nearby. Studies link green offices to fewer sick days and sharper focus.</p>
    <div class="round" role="img" aria-label="Close-up of a leafy plant" style="left:108px;top:175px"></div>
    <div class="round" role="img" aria-label="Close-up of a succulent" style="left:168px;top:175px"></div>
    <div class="round" role="img" aria-label="Close-up of a fern" style="left:228px;top:175px"></div>
  </div>
  <div class="page right">
    <h2 class="heading" style="position:absolute;left:22px;top:14px;font-size:13px">Plant Gallery</h2>
    <div class="gallery">
      <div class="plant"><div class="pot" role="img" aria-label="Potted ficus"></div><span>Ficus</span></div>
      <div class="plant"><div class="pot" role="img" aria-label="Potted zamia"></div><span>Zamia</span></div>
      <div class="plant"><div class="pot" role="img" aria-label="Potted sansevieria"></div><span>Sansevieria</span></div>
      <div class="plant"><div class="pot" role="img" aria-label="Potted kentia palm"></div><span>Kentia</span></div>
      <div class="plant"><div class="pot" role="img" aria-label="Potted monstera"></div><span>Monstera</span></div>
      <div class="plant"><div class="pot" role="img" aria-label="Potted calathea"></div><span>Calathea</span></div>
      <div class="plant"><div class="pot" role="img" aria-label="Potted aglaonema"></div><span>Aglaonema</span></div>
      <div class="plant"><div class="pot" role="img" aria-label="Potted dracaena"></div><span>Dracaena</span></div>
      <div class="plant"><div class="pot" role="img" aria-label="Potted pothos"></div><span>Pothos</span></div>
      <div class="plant"><div class="pot" role="img" aria-label="Potted philodendron"></div><span>Philodendron</span></div>
      <div class="plant"><div class="pot" role="img" aria-label="Potted yucca"></div><span>Yucca</span></div>
      <div class="plant"><div class="pot" role="img" aria-label="Potted aspidistra"></div><span>Aspidistra</span></div>
    </div>
    <div class="edge-strip"></div>
  </div>
</section>

</body>
</html>
```